Seafood Retailer requires varies packaging labels

We are an established business (Restaurant, Seafood Retailer and Crayfish Wholesaler). We have just got a new logo which covers all three aspects of our business (via Artbazaar!). We have always sold cellar door but have been asked by several food outlets to stock our product but as you will see from our pictures - it needs some serious work to take us to the next level. We have a well known finer dining restaurant which we use all these products in and is how several products came about on our Seafood shop shelves. The products are of high quality (just not the labelling). We now want to package our Seafood Retail Shop with professional packaging and labelling and reflect the "quality and freshness" of our products. We have several items we want to label as per below.

If we were to use a slogan it would be "Its about the Freshness and Quality" but not necessary.

We are after a label for our Pickled Seafood 350g tub (Various) - conical container 9cm high x 9cm (top), 7cm (bottom) ONLY but will also try and utilise it to be consistent with the other products following.

Salt and Pepper MIx 250g - conical container (as above)
Smoked Fish (Various weight & fish) - 21cm x 25cm vacuum sealed bags.
Kilpatrick Sauce 250ml - square bottle 22cm high x 4.5cm wide
Minty Lime Vinaigrette 250ml - 23cm round bottle - 4.7cm dia.
Smoked Spicy Salt 75g- 13cm wide x 16cm high vacuum bag
Dukkah 75g - 13cm wide x 16cm high vacuum bag
Lobster Oil 150ml - 18cm x 4.5cm dia round bottle

We will need a working file so we can change the names for the pickled seafood as needed.

I have attached photos of our current products for true understanding of what we currently have had to get by and where we wish to go.

We have a label printer that can print black type overs eg the name of each product so we can have generic coloured labels which we can print over with the change of each product.

We want something that will become a recognisable label.
Updates

Attn Designers.
We are only after one design but which we will use as a guide for all the options supplied as a starting point. The Pickled containers will probably be where we start but happy with any submissions. I probably wasnt very clear but wanted to show all the things we will be using the labelling for so that we can get some continuity We are just after some direction on a good look.  Thanks Melda

Reason: Had some technical problems and wish to extend the time to allow more time conversing with designers.

Target Market(s)

Our target market varies but generally 30 - 65 years in the more affluent background. We are located "literally in the middle of a paddock in the middle of nowhere" (near several holiday villages) and it is the reputation of our premium, fresh products that have people returning and amazed on their first experience.

Industry/Entity Type

Restaurant

Requirements
Must have
• All:

Our logo and the colours are:
Orange
C 13%
M 79%
Y 100%
K 3%

Blue
C 100%
M 96%
Y 14%
K 3%

weight

nutrition panel, barcode (but we can also do that as a separate label on the back ourselves if needed)

"Produced & packaged by:
Copper Reef Foods Pty Ltd, 40271 Danvers Highway, Millicoon SA 5630
Ph: 08 87316042"

Made in Australia from local and imported ingredients. Keep refrigerated. Store at 1oC - 4oC. Use in 7 days after opening.

Nice to have
• Pickled seafood - "Gourmet Pickled" and "Ready to Eat"
Should not have
• Use only the "Copper Reef Foods" logo (not the "Copper Reef Restaurant & Seafood Sales or Restaurant Only logos)

```html
<!DOCTYPE html>
<html lang="en">
<head>
<meta charset="utf-8">
<title>Copper Reef Foods – Product Labels</title>
<link rel="stylesheet" href="https://fonts.googleapis.com/css2?family=Cinzel:wght@400;500&family=Tinos:wght@700&display=swap">
<style>
  :root {
    --brand-blue: #2c3583;
    --brand-orange: #d2582a;
    --label-white: #ffffff;
    --page-bg: #ffffff;
  }
  html, body {
    margin: 0;
    padding: 0;
    width: 1056px;
    height: 1200px;
    overflow: hidden;
    background: var(--page-bg);
  }
  .label-sheet {
    display: block;
    width: 1056px;
    height: 1200px;
  }
  .label {
    filter: drop-shadow(3px 4px 5px rgba(0, 0, 0, 0.35));
  }
  .label-base { fill: var(--label-white); }
  .label-band { fill: var(--brand-blue); }
  .label-swoosh { fill: none; stroke: var(--brand-blue); stroke-linecap: round; }
  .brand-name {
    font-family: "Cinzel", serif;
    font-weight: 500;
    fill: var(--brand-orange);
    text-anchor: middle;
  }
  .brand-dot { fill: var(--brand-orange); }
  .product-name {
    font-family: "Cinzel", serif;
    font-weight: 400;
    fill: var(--label-white);
    text-anchor: middle;
  }
  .product-variant {
    font-family: "Cinzel", serif;
    font-weight: 400;
    fill: var(--label-white);
    text-anchor: middle;
    letter-spacing: 1px;
  }
  .net-quantity {
    font-family: "Tinos", serif;
    font-weight: 700;
    fill: var(--label-white);
    text-anchor: middle;
  }
</style>
</head>
<body>
<svg class="label-sheet" viewBox="0 0 1056 1200" xmlns="http://www.w3.org/2000/svg">
  <defs>
    <clipPath id="tub-shape">
      <path d="M137,337 H547 Q572,337 570,362 L547,753 Q545,778 520,778 H185 Q160,778 158,753 L114,362 Q112,337 137,337 Z"/>
    </clipPath>
    <clipPath id="bottle-shape">
      <rect x="690" y="63" width="228" height="1067" rx="26"/>
    </clipPath>
  </defs>

  <!-- Pickled seafood tub label -->
  <g class="label tub-label">
    <g clip-path="url(#tub-shape)">
      <rect class="label-base" x="100" y="330" width="480" height="460"/>
      <path class="label-band" d="M100,580 C170,560 230,540 290,545 C380,552 470,572 590,563 V790 H100 Z"/>
      <path class="label-swoosh" stroke-width="7" d="M120,560 C190,538 240,524 290,527 C370,533 460,556 580,555"/>
    </g>
    <circle class="brand-dot" cx="168" cy="428" r="7"/>
    <text class="brand-name" x="350" y="443" font-size="44">Copper Reef</text>
    <text class="brand-name" x="342" y="500" font-size="19">Foods</text>
    <text class="product-name" x="342" y="645" font-size="33">Pickled Seafood</text>
    <text class="product-variant" x="345" y="686" font-size="20">omomomomo</text>
    <text class="net-quantity" x="342" y="758" font-size="21">350g</text>
  </g>

  <!-- Kilpatrick sauce bottle label -->
  <g class="label bottle-label">
    <g clip-path="url(#bottle-shape)">
      <rect class="label-base" x="690" y="63" width="228" height="1067"/>
      <path class="label-band" d="M680,322 C730,312 770,303 810,306 C850,309 880,316 930,314 V1140 H680 Z"/>
      <path class="label-swoosh" stroke-width="6" d="M685,305 C730,296 770,290 810,292 C850,295 880,302 925,301"/>
    </g>
    <text class="brand-name" x="804" y="146" font-size="28">Copper Reef</text>
    <text class="brand-name" x="802" y="175" font-size="13">Foods</text>
    <text class="product-name" font-size="52" transform="translate(826 665) rotate(-90)">Kilpatrick Sauce</text>
    <text class="product-variant" x="806" y="1009" font-size="19">omomomom</text>
    <text class="net-quantity" x="810" y="1106" font-size="21">250mL</text>
  </g>
</svg>
</body>
</html>
```